We Import and supply LED Lighting products (High Bays, Flood Lights, Bulbs, Down Lights, Strip Lighting, Night Lights.) and we are after a brochure design that communicates these product points below..

1. Environmentally Friendly.
2. Recyclable
3. Energy Saving
3. Cost Savings for the customer (big and small business)
4. Long Life Span.
5. Lower Maintenance Costs.
6. Importing
7. QUALITY PRODUCTS

The brochure needs to reflect that LED lighting is a safer 'lighting' solution for the environment and also to reflect big cost savings to big and small business ... I have highlighted some colours below but will leave this to the designer to decide on.

I have included some photos that resemble the type of other LED Lighting we sell.

Kind Regards

File 3 & File 5 can't be opened so please ignore.

Target Market(s)

Industrial / Warehousing... (Highbays & Flood Lights)
Domestic: ..... Bulbs & Strip Lighting

Industry/Entity Type

Small Business

Requirements
Must have
• Your professional experience in graphic design... show me that you can produce a professional look, not just a rush job with bad spelling.

Definitely depicts that we sell Quality LED Lighting with very competitive pricing.

Wholesale and Retail.

Our Logo.. this is the image I have uploaded, '"purple circle with grey wings"
Nice to have
• images and or symbols that depict recyclable, environmentally safe. energy saving and maybe a stack of coins that show money that can be saved (especially on the highbays)
Should not have
• copying the brochure I have uploaded and just adding colour!...

```html
<!DOCTYPE html>
<html lang="en">
<head>
<meta charset="utf-8">
<title>LED Lighting Brochure</title>
<link href="https://fonts.googleapis.com/css2?family=Oswald:wght@500&family=Ubuntu:wght@700&family=Open+Sans:wght@400&display=swap" rel="stylesheet">
<style>
:root{
  --stage:#e6e6e6;
  --paper:#ffffff;
  --leaf:#8cc63f;
  --leaf-dark:#6fae2c;
  --grass-deep:#2f5a12;
  --grass-mid:#6a9a2a;
  --grass-light:#b9d77a;
  --plum:#8a2a8c;
  --ink:#333333;
  --rule:#b5b5b5;
  --photo-grey:#cfd2d4;
}
*{margin:0;padding:0;box-sizing:border-box}
html,body{width:1200px;height:800px;overflow:hidden}
body{background:var(--stage);font-family:"Open Sans",Arial,sans-serif;color:var(--ink)}
.brochure{position:absolute;left:60px;top:60px;width:1080px;height:680px;background:var(--paper);box-shadow:0 6px 24px rgba(0,0,0,.18);display:flex;flex-direction:column}
.banner{position:relative;height:200px;flex:none;background:linear-gradient(180deg,var(--grass-light) 0%,var(--grass-mid) 45%,var(--grass-deep) 100%)}
.banner-claims{position:absolute;inset:0;display:grid;grid-template-columns:repeat(3,1fr);align-items:center;text-align:center}
.claim{font-family:"Oswald",Impact,sans-serif;font-weight:500;font-size:34px;line-height:1.25;color:#fff;text-transform:uppercase;text-shadow:0 2px 6px rgba(0,0,0,.35)}
.panels{flex:1;display:grid;grid-template-columns:repeat(3,1fr);min-height:0}
.panel{padding:18px 22px 10px;border-right:1px solid #e4e4e4;display:flex;flex-direction:column;min-height:0}
.panel:last-child{border-right:0}
.product{display:flex;gap:16px;flex:1;padding:8px 0;min-height:0}
.product + .product{border-top:1px dashed var(--rule)}
.product-photo{flex:none;background:linear-gradient(180deg,#e9eaeb,var(--photo-grey))}
.product-photo.green{background:linear-gradient(180deg,#a9d46a,var(--leaf-dark))}
.product-photo.strip{background:linear-gradient(180deg,#eeeeee,#c9c9cf)}
.product-photo.soft{background:linear-gradient(180deg,#f5f5f5,#e2e2e2)}
.product-photo.night{background:linear-gradient(180deg,#f3d7ea,#c78ab8)}
.product-title{font-family:"Ubuntu",Arial,sans-serif;font-weight:700;font-size:19px;color:var(--plum);margin:4px 0 10px;white-space:nowrap}
.specs{display:grid;grid-template-columns:90px 1fr;column-gap:6px;font-size:7.5px;line-height:1.45}
.specs dt,.specs dd{margin:0;white-space:nowrap}
.footer-band{height:40px;flex:none;background:linear-gradient(180deg,var(--leaf),var(--leaf-dark))}
</style>
</head>
<body>
<article class="brochure">
  <header class="banner" role="img" aria-label="Close-up photograph of fresh green grass with clover flowers">
    <div class="banner-claims">
      <p class="claim">Environmentally<br>Friendly</p>
      <p class="claim">Big Reduction<br>Power Costs</p>
      <p class="claim">2 Year<br>Warranty</p>
    </div>
  </header>

  <main class="panels">
    <section class="panel">
      <div class="product">
        <div class="product-photo" style="width:110px;height:180px" role="img" aria-label="Photo of an LED high bay lamp"></div>
        <div>
          <h2 class="product-title">Highbays</h2>
          <dl class="specs">
            <dt>Input Voltage</dt><dd>AC100-265V/50-60Hz</dd>
            <dt>Light Source</dt><dd>LED Chip – Lumora</dd>
            <dt></dt><dd>45 mil COB</dd>
            <dt>Consumption</dt><dd>100W/150W/200W</dd>
            <dt>Luminous Efficiency</dt><dd>90-100 lm/W</dd>
            <dt>Beam Angles Available</dt><dd>45°/90°/120°</dd>
            <dt>Colour Temperature</dt><dd>2800K-6500K</dd>
            <dt>Driver</dt><dd>Voltara</dd>
            <dt>Power Factor</dt><dd>&gt;0.97</dd>
            <dt>Working Life-Span</dt><dd>&gt;50,000 Hrs</dd>
          </dl>
        </div>
      </div>
      <div class="product">
        <div class="product-photo soft" style="width:110px;height:160px" role="img" aria-label="Photo of an LED bulb"></div>
        <div>
          <h2 class="product-title">Bulbs</h2>
          <dl class="specs">
            <dt>Power Consumption</dt><dd>3W / 5W / 7W / 9W</dd>
            <dt>Base Type</dt><dd>B22 / E27</dd>
            <dt>Input Voltage</dt><dd>AC110 - 240V</dd>
            <dt>Colour</dt><dd>Cool or Warm White</dd>
            <dt>Colour Temp</dt><dd>2800 - 6500 K</dd>
          </dl>
        </div>
      </div>
    </section>

    <section class="panel">
      <div class="product">
        <div class="product-photo green" style="width:110px;height:180px" role="img" aria-label="Photo of an LED flood light"></div>
        <div>
          <h2 class="product-title">Flood Lights</h2>
          <dl class="specs">
            <dt>Input Voltage</dt><dd>AC100-265V/50-60Hz</dd>
            <dt>Light Source</dt><dd>LED Chip – Lumora</dd>
            <dt></dt><dd>45 mil COB</dd>
            <dt>Consumption</dt><dd>100W/150W/200W</dd>
            <dt>Luminous Efficiency</dt><dd>90-100 lm/W</dd>
            <dt>Beam Angles Available</dt><dd>45°/90°/120°</dd>
            <dt>Colour Temperature</dt><dd>2800K-6500K</dd>
            <dt>Driver</dt><dd>Voltara</dd>
            <dt>Power Factor</dt><dd>&gt;0.97</dd>
            <dt>Working Life-Span</dt><dd>&gt;50,000 Hrs</dd>
          </dl>
        </div>
      </div>
      <div class="product">
        <div class="product-photo strip" style="width:110px;height:160px" role="img" aria-label="Photo of a reel of colourful LED strip lighting"></div>
        <div>
          <h2 class="product-title">Strip Lighting</h2>
          <dl class="specs">
            <dt>Power Consumption</dt><dd>3W / 5W / 7W / 9W</dd>
            <dt>Base Type</dt><dd>B22 / E27</dd>
            <dt>Input Voltage</dt><dd>AC110 - 240V</dd>
            <dt>Colour</dt><dd>Cool or Warm White</dd>
            <dt>Colour Temp</dt><dd>2800 - 6500 K</dd>
          </dl>
        </div>
      </div>
    </section>

    <section class="panel">
      <div class="product" style="flex:1.5">
        <div class="product-photo soft" style="width:100px;height:90px" role="img" aria-label="Photo of a COB LED downlight"></div>
        <div>
          <h2 class="product-title">COB Downlights</h2>
          <dl class="specs">
            <dt>Input Voltage</dt><dd>AC100-265V/50-60Hz</dd>
            <dt>Light Source</dt><dd>LED Chip – Lumora</dd>
            <dt></dt><dd>45 mil COB</dd>
            <dt>Consumption</dt><dd>100W/150W/200W</dd>
            <dt>Luminous Efficiency</dt><dd>90-100 lm/W</dd>
            <dt>Beam Angles Available</dt><dd>45°/90°/120°</dd>
            <dt>Colour Temperature</dt><dd>2800K-6500K</dd>
            <dt>Driver</dt><dd>Voltara</dd>
            <dt>Power Factor</dt><dd>&gt;0.97</dd>
            <dt>Working Life-Span</dt><dd>&gt;50,000 Hrs</dd>
          </dl>
        </div>
      </div>
      <div class="product">
        <div class="product-photo soft" style="width:100px;height:80px" role="img" aria-label="Photo of a small LED deck light"></div>
        <div>
          <h2 class="product-title">Deck Lighting</h2>
          <dl class="specs">
            <dt>Power Consumption</dt><dd>3W / 5W / 7W / 9W</dd>
            <dt>Base Type</dt><dd>B22 / E27</dd>
            <dt>Input Voltage</dt><dd>AC110 - 240V</dd>
            <dt>Colour</dt><dd>Cool or Warm White</dd>
            <dt>Colour Temp</dt><dd>2800 - 6500 K</dd>
          </dl>
        </div>
      </div>
      <div class="product">
        <div class="product-photo night" style="width:100px;height:80px" role="img" aria-label="Photo of a plush night light toy with projected light patterns"></div>
        <div>
          <h2 class="product-title">Night Lights</h2>
          <dl class="specs">
            <dt>Power Consumption</dt><dd>3W / 5W / 7W / 9W</dd>
            <dt>Base Type</dt><dd>B22 / E27</dd>
            <dt>Input Voltage</dt><dd>AC110 - 240V</dd>
            <dt>Colour</dt><dd>Cool or Warm White</dd>
            <dt>Colour Temp</dt><dd>2800 - 6500 K</dd>
          </dl>
        </div>
      </div>
    </section>
  </main>

  <footer class="footer-band"></footer>
</article>
</body>
</html>
```